Marnie Lux Business Card Design

I need a business card for my daughter. She has it all described in the file below. But it needs to be square in shape. http://www.marnielux.com is her web site

Target Market(s)

18-35 year old women

Industry/Entity Type

Fashion

Contact Information for Business Card

Please look at the attached file as it has all the details.

Requirements
Must have
• Please look at the attached file as it has all the details.
Nice to have
Should not have

```html
<!DOCTYPE html>
<html lang="en">
<head>
<meta charset="utf-8">
<title>Marnie Lux – Business Card Back</title>
<link href="https://fonts.googleapis.com/css2?family=Nunito+Sans:wght@700;800&family=EB+Garamond&family=Playfair+Display:wght@700&display=swap" rel="stylesheet">
<style>
  :root {
    --ink: #111111;
    --paper: #ffffff;
    --card-pink: #cea6bf;
    --tag-text: #e8cdd8;
    --label-white: #ffffff;
  }
  html, body {
    margin: 0;
    padding: 0;
    width: 1200px;
    height: 1000px;
    overflow: hidden;
    background: var(--paper);
  }
  .canvas {
    position: relative;
    width: 1200px;
    height: 1000px;
  }
  .side-title {
    position: absolute;
    top: 114px;
    left: 0;
    width: 1200px;
    text-align: center;
    margin: 0;
    font-family: "Nunito Sans", sans-serif;
    font-weight: 800;
    font-size: 37px;
    letter-spacing: 3px;
    color: var(--ink);
    line-height: 1;
  }
  .card-frame {
    position: absolute;
    left: 250px;
    top: 200px;
    width: 700px;
    height: 700px;
    background: var(--ink);
  }
  .card {
    position: absolute;
    left: 19px;
    top: 19px;
    width: 662px;
    height: 662px;
    background: var(--card-pink);
  }
  .tagline {
    position: absolute;
    left: 40px;
    top: 82px;
    width: 582px;
    height: 64px;
    background: var(--ink);
    color: var(--tag-text);
    font-family: "EB Garamond", serif;
    font-size: 30px;
    line-height: 64px;
    text-align: center;
    white-space: nowrap;
  }
  .contact-list {
    position: absolute;
    left: 40px;
    top: 182px;
    margin: 0;
    padding: 0;
    list-style: none;
  }
  .contact-item {
    display: flex;
    align-items: center;
    height: 58px;
    margin-bottom: 8px;
  }
  .contact-icon {
    width: 58px;
    height: 58px;
    flex: none;
  }
  .contact-text {
    margin-left: 25px;
    font-family: "Nunito Sans", sans-serif;
    font-weight: 800;
    font-size: 31px;
    color: var(--ink);
    white-space: nowrap;
  }
  .links {
    position: absolute;
    left: 40px;
    top: 466px;
  }
  .link-row {
    display: flex;
    align-items: baseline;
    height: 52px;
    white-space: nowrap;
  }
  .link-label {
    font-family: "Playfair Display", serif;
    font-weight: 700;
    font-size: 34px;
    letter-spacing: 2px;
    color: var(--label-white);
  }
  .link-url {
    font-family: "Nunito Sans", sans-serif;
    font-weight: 800;
    font-size: 31px;
    color: var(--ink);
  }
  .blog .link-url { margin-left: 16px; }
  .video .link-url { margin-left: 10px; }
</style>
</head>
<body>
<div class="canvas">
  <h1 class="side-title">BACK</h1>
  <div class="card-frame">
    <div class="card">
      <div class="tagline">blogger &amp; vidlooper // beauty - fashion - travel</div>
      <ul class="contact-list">
        <li class="contact-item">
          <svg class="contact-icon" viewBox="0 0 58 58" aria-hidden="true"><circle cx="29" cy="29" r="29" fill="var(--ink)"/></svg>
          <span class="contact-text">pictora.com/marnieluxxo</span>
        </li>
        <li class="contact-item">
          <svg class="contact-icon" viewBox="0 0 58 58" aria-hidden="true"><circle cx="29" cy="29" r="29" fill="var(--ink)"/></svg>
          <span class="contact-text">chirply.com/marnieluxxo</span>
        </li>
        <li class="contact-item">
          <svg class="contact-icon" viewBox="0 0 58 58" aria-hidden="true"><circle cx="29" cy="29" r="29" fill="var(--ink)"/></svg>
          <span class="contact-text">@marnieluxxo</span>
        </li>
        <li class="contact-item">
          <svg class="contact-icon" viewBox="0 0 58 58" aria-hidden="true">
            <circle cx="29" cy="29" r="29" fill="var(--ink)"/>
            <rect x="13" y="18" width="32" height="23" rx="1.5" fill="var(--paper)"/>
            <polyline points="13,19 29,32 45,19" fill="none" stroke="var(--ink)" stroke-width="2.5"/>
            <line x1="13" y1="41" x2="24" y2="29" stroke="var(--ink)" stroke-width="2"/>
            <line x1="34" y1="29" x2="45" y2="41" stroke="var(--ink)" stroke-width="2"/>
          </svg>
          <span class="contact-text">marnie@marnielux.com</span>
        </li>
      </ul>
      <div class="links">
        <div class="link-row blog"><span class="link-label">BLOG:</span><span class="link-url">marnielux.com</span></div>
        <div class="link-row video"><span class="link-label">VIDLOOP:</span><span class="link-url">vidloop.com/marnielux</span></div>
      </div>
    </div>
  </div>
</div>
</body>
</html>
```